Brindlewick Music Studio needs a promotional postcard design

We are looking for a postcard design for a small business that provides clients with private music lesson instruction. We are looking for a design that will convey the message of "music is fun for kids" that will appeal to parents and encourage them to sign up. We have a company logo that should be used and our color scheme is teal and turquoise. All of our contact info should be displayed as well.

Target Market(s)

Parents with young kids

Contact Information for Business Card

web: www.brindlewickmusicstudio.example
email: lessons@brindlewickmusicstudio.example
phone: 202-555-0147

Font styles to use
Serif
Sans Serif

Colors
33b8a4
86cfc6
0456a4
87cfc6

Requirements
Must have
• Music lessons in your home
• Creating little stars one at a time
• Sign Up Now
• Please use these images:
Nice to have
• Something like this sample postcard:

```html
<!DOCTYPE html>
<html lang="en">
<head>
<meta charset="utf-8">
<title>Brindlewick Music Studio – Postcard</title>
<link rel="stylesheet" href="https://fonts.googleapis.com/css2?family=Prata&family=Montserrat:wght@500&family=Oswald:wght@400;700&family=Yellowtail&family=Passion+One:wght@700&display=swap">
<style>
  :root {
    --teal: #50b8bd;
    --teal-bright: #4cc0c6;
    --navy: #0e2430;
    --ink: #111111;
    --white: #ffffff;
    --stage: #0b0a0c;
    --backdrop: #eceae6;
    --rule: #cfcfcf;
  }
  * { box-sizing: border-box; margin: 0; padding: 0; }
  html, body { width: 1200px; height: 698px; overflow: hidden; background: var(--backdrop); }
  .canvas { position: relative; width: 1200px; height: 698px; }

  .card { position: absolute; top: 149px; width: 480px; height: 400px; overflow: hidden;
          box-shadow: 0 2px 6px rgba(0,0,0,.25); }
  .card--front { left: 106px; background: var(--stage); }
  .card--back { left: 615px; background: var(--white); }

  .brand-dot { position: absolute; border-radius: 50%; }
  .brand-name { position: absolute; font-family: "Prata", serif; font-weight: 400; white-space: nowrap; line-height: 1; }
  .brand-tag { position: absolute; font-family: "Montserrat", sans-serif; font-weight: 500;
               letter-spacing: .42em; white-space: nowrap; line-height: 1; }

  /* front */
  .front-header { position: absolute; left: 0; top: 0; width: 480px; height: 85px; background: var(--teal); }
  .front-header .brand-dot { left: 106px; top: 7px; width: 70px; height: 70px; border: 3px solid var(--white); }
  .front-header .brand-name { left: 194px; top: 14px; font-size: 34px; color: var(--white); }
  .front-header .brand-tag { left: 196px; top: 57px; font-size: 10px; color: var(--white); }

  .front-photo { position: absolute; left: 0; top: 85px; width: 480px; height: 315px;
                 background: radial-gradient(ellipse at 35% 40%, #4a3a3c 0%, #2a2024 45%, #0b0a0c 100%); }

  .headline { position: absolute; left: 262px; top: 212px; width: 184px; text-align: center;
              color: var(--teal-bright); font-weight: 400; }
  .headline span { position: absolute; left: 0; width: 184px; white-space: nowrap; }
  .headline__script { top: 0; font-family: "Yellowtail", cursive; font-size: 44px; line-height: 44px; }
  .headline__fun { top: 44px; font-family: "Passion One", sans-serif; font-weight: 700; font-size: 86px; line-height: 76px; letter-spacing: 2px; }
  .headline__kids { top: 126px; font-family: "Passion One", sans-serif; font-weight: 700; font-size: 34px; line-height: 34px; letter-spacing: 1px; }

  /* back */
  .back-panel { position: absolute; left: 0; top: 0; width: 228px; height: 400px; background: var(--teal); }
  .back-photo { position: absolute; left: 14px; top: 242px; width: 160px; height: 158px;
                background: linear-gradient(180deg, #6a5a52 0%, #2c2c34 60%, #1a1a22 100%); }
  .back-brand .brand-dot { left: 75px; top: 26px; width: 78px; height: 78px; background: var(--navy); }
  .back-brand .brand-name { left: 0; top: 112px; width: 228px; text-align: center; font-size: 30px; color: var(--navy); }
  .back-brand .brand-tag { left: 0; top: 152px; width: 228px; text-align: center; font-size: 10px;
                           color: var(--navy); padding-left: .42em; }
  .contact { position: absolute; left: 0; top: 174px; width: 228px; text-align: center; color: var(--ink); font-style: normal; }
  .contact__phone { display: block; font-family: "Oswald", sans-serif; font-weight: 700; font-size: 22px; line-height: 26px; }
  .contact__line { display: block; font-family: "Oswald", sans-serif; font-weight: 400; font-size: 9.5px;
                   text-transform: uppercase; line-height: 14px; white-space: nowrap; }

  .stamp { position: absolute; left: 391px; top: 37px; width: 50px; height: 50px; border: 1px solid var(--rule); }
  .address-to { position: absolute; left: 277px; top: 105px; font-family: "Montserrat", sans-serif; font-size: 9px; color: var(--ink); }
  .address-line { position: absolute; left: 287px; width: 153px; height: 1px; background: var(--rule); }
</style>
</head>
<body>
<main class="canvas">

  <section class="card card--front" aria-label="Postcard front">
    <header class="front-header">
      <span class="brand-dot"></span>
      <span class="brand-name">Brindlewick</span>
      <span class="brand-tag">MUSIC STUDIO</span>
    </header>
    <div class="front-photo" role="img" aria-label="Photo of children and their teacher gathered on a stage after a recital"></div>
    <h1 class="headline">
      <span class="headline__script">music is</span>
      <span class="headline__fun">FUN</span>
      <span class="headline__kids">FOR KIDS</span>
    </h1>
  </section>

  <section class="card card--back" aria-label="Postcard back">
    <div class="back-panel"></div>
    <div class="back-photo" role="img" aria-label="Photo of a smiling girl making a peace sign"></div>
    <div class="back-brand">
      <span class="brand-dot"></span>
      <span class="brand-name">Brindlewick</span>
      <span class="brand-tag">MUSIC STUDIO</span>
    </div>
    <address class="contact">
      <span class="contact__phone">202-555-0147</span>
      <span class="contact__line">lessons@brindlewickmusicstudio.example</span>
      <span class="contact__line">www.brindlewickmusicstudio.example</span>
    </address>
    <div class="stamp"></div>
    <span class="address-to">To</span>
    <span class="address-line" style="top:145px"></span>
    <span class="address-line" style="top:169px"></span>
    <span class="address-line" style="top:191px"></span>
    <span class="address-line" style="top:216px"></span>
  </section>

</main>
</body>
</html>
```